Harbor Lynx Associates Flyer

Create a tri-fold brochure for Harbor Lynx Associates. I am getting a new logo - waiting on the final file. I've attached the copy.

Target Market(s)

retail energy companies and retail energy brokers

Industry/Entity Type

energy

Font styles to use
Serif

Colors
0054AA
0677BA
7BADD7
CADEEF
E8F1F8

Requirements
Must have
• I will be uploading a picture of myself and my partner - that should be somewhere in the inside.
Nice to have
• follow the color scheme of the logo
Should not have
• no mine pictures -use energy pictures - power lines etc. office picture and picture of 2 businesspeople shaking hands

```html
<!DOCTYPE html>
<html lang="en">
<head>
<meta charset="utf-8">
<title>Harbor Lynx Associates – Tri-fold Brochure</title>
<link rel="stylesheet" href="https://fonts.googleapis.com/css2?family=Merriweather:ital,wght@0,400;0,700;0,900;1,700&family=Noto+Serif:ital,wght@0,400;0,700;1,700&display=swap">
<style>
:root{
  --navy:#0054AA;
  --blue:#0677BA;
  --sky:#7BADD7;
  --pale:#CADEEF;
  --mist:#E8F1F8;
  --contact:#0E5CB6;
  --ink:#111111;
  --text:#2b2b2b;
  --page:#e4e6e9;
  --white:#ffffff;
}
*{box-sizing:border-box;margin:0;padding:0}
html,body{width:1200px;height:992px;overflow:hidden}
body{background:var(--page);font-family:"Noto Serif",Georgia,serif;color:var(--text)}
.spread{position:absolute;left:290px;width:620px;height:480px;display:grid;grid-template-columns:207px 206px 207px;background:var(--white);box-shadow:0 4px 14px rgba(0,0,0,.18);overflow:hidden}
.spread--outside{top:12px}
.spread--inside{top:500px}
.panel{position:relative;overflow:hidden}
.photo{position:absolute;display:block}

/* brand name stand-in */
.brand{display:flex;flex-direction:column;align-items:center;font-family:"Merriweather",Georgia,serif;font-weight:900;letter-spacing:.06em;line-height:1.15;text-align:center}
.brand__dot{width:22px;height:22px;border-radius:50%;background:currentColor;margin-bottom:6px}
.brand__name{font-size:13px}
.brand__sub{font-size:8px;letter-spacing:.28em}

/* testimonials */
.testimonials__body{position:absolute;left:20px;right:18px;top:152px}
.testimonials__title{font-family:"Merriweather",Georgia,serif;font-weight:400;color:var(--blue);font-size:10.5px;line-height:1.25;margin-bottom:10px}
.quote{font-size:6.4px;line-height:1.6;color:var(--text)}
.quote__by{display:block;text-align:right;font-style:italic;font-weight:700;font-size:6.2px;color:var(--ink);margin-top:2px}
.quote-rule{display:flex;align-items:center;gap:5px;margin:7px 0 8px}
.quote-rule::before,.quote-rule::after{content:"";flex:1;border-top:1px dotted #777}
.quote-rule__mark{font-family:"Merriweather",serif;font-weight:900;color:var(--sky);font-size:14px;line-height:.6;height:8px}

/* contact */
.panel--contact{background:linear-gradient(160deg,var(--contact) 0%,#0b58b0 60%,#0a4fa0 100%);color:var(--white);text-align:center}
.panel--contact .brand{margin-top:26px}
.contact__title{font-family:"Merriweather",Georgia,serif;font-weight:400;font-size:11px;margin-top:26px;letter-spacing:.03em}
.contact__rule{width:22px;height:2px;background:var(--sky);margin:7px auto 14px}
.contact__list{list-style:none;display:flex;flex-direction:column;align-items:center;gap:9px}
.contact__item{display:flex;flex-direction:column;align-items:center;gap:6px;font-size:6.8px}
.contact__item--phone{font-family:"Merriweather",serif;font-size:10.5px}
.icon{width:26px;height:26px;border-radius:50%;background:var(--ink);border:2px solid var(--white);display:flex;align-items:center;justify-content:center}
.icon svg{width:13px;height:13px}

/* cover */
.cover__logo{position:absolute;top:14px;left:0;right:0;color:var(--ink)}
.cover__url{position:absolute;left:0;right:0;top:290px;height:15px;background:var(--ink);color:var(--white);font-size:7px;letter-spacing:.02em;display:flex;align-items:center;justify-content:center}
.cover__stripes{position:absolute;left:0;right:0;top:305px;bottom:0;background:repeating-linear-gradient(90deg,#fff 0 6px,#f3f5f8 6px 8px)}
.cover__headline{position:absolute;left:20px;top:318px;font-family:"Merriweather",Georgia,serif;font-weight:700;font-size:14px;line-height:1.1;color:var(--ink)}
.cover__headline .accent{color:var(--navy)}

/* inside */
.panel--about{background:linear-gradient(180deg,#fff 0%,var(--mist) 100%)}
.about__rule{position:absolute;left:18px;top:22px;width:17px;height:2px;background:var(--sky)}
.about__kicker{position:absolute;left:18px;top:27px;font-family:"Merriweather",serif;color:var(--blue);font-size:9px;letter-spacing:.04em}
.about__title{position:absolute;left:18px;top:42px;font-family:"Merriweather",serif;font-weight:700;color:var(--blue);font-size:15.5px;line-height:1.12}
.about__text{position:absolute;left:18px;right:14px;top:84px;font-size:5.9px;line-height:1.62;color:var(--text)}
.about__text p+p{margin-top:7px}
.panel--mission{background:linear-gradient(180deg,#fff 0%,var(--mist) 100%)}
.panel--mission .brand{color:var(--ink);margin-top:28px}
.mission__text{position:absolute;left:12px;right:12px;top:112px;font-size:5.7px;line-height:1.62;color:var(--text)}
.inside-art{position:absolute;left:0;top:0;width:620px;height:480px;pointer-events:none;z-index:1}
.office{position:absolute;left:26px;top:348px;width:100px;height:100px;border-radius:50%;border:5px solid var(--sky);background:radial-gradient(circle at 40% 35%,#dfe7ef 0%,#9fb1c4 55%,#5c6f84 100%);z-index:2}
</style>
</head>
<body>

<!-- Outside spread -->
<section class="spread spread--outside" aria-label="Brochure outside">
  <article class="panel panel--testimonials">
    <svg class="photo" style="left:0;top:0" width="207" height="150" viewBox="0 0 207 150">
      <defs>
        <linearGradient id="suitGrad" x1="0" y1="0" x2="1" y2="1">
          <stop offset="0" stop-color="#2c4766"/><stop offset=".6" stop-color="#17263a"/><stop offset="1" stop-color="#0d1826"/>
        </linearGradient>
      </defs>
      <path d="M0 0H207V100Q110 150 0 118Z" fill="url(#suitGrad)" role="img" aria-label="Photo of a businessman in a suit tapping a five-star rating"/>
      <path d="M0 118Q110 150 207 100V110Q110 160 0 128Z" fill="var(--sky)"/>
      <path d="M0 128Q110 160 207 110V116Q110 166 0 134Z" fill="var(--ink)"/>
    </svg>
    <div class="testimonials__body">
      <h2 class="testimonials__title">Here’s what some of<br>our clients are saying:</h2>
      <p class="quote">“Marcus Whitlow &amp; Harbor Lynx Associates found us the perfect candidate and they did it quickly. If you’re an REP looking for great talent, you should use HLA”<span class="quote__by">Evan Pryce, BrightGrid Energy</span></p>
      <div class="quote-rule"><span class="quote-rule__mark">“</span></div>
      <p class="quote">“Harbor Lynx Associates helped TPS quickly find a great candidate for an essential position that we need to fill right away”.<span class="quote__by">Laura Denton,<br>Tailored Power Solutions</span></p>
      <div class="quote-rule"><span class="quote-rule__mark">“</span></div>
      <p class="quote">“Harbor Lynx Associates helped OPK quickly find a great person for our team. Marcus Whitlow has more connections than just about anyone else in the industry”.<span class="quote__by">Owen Carver, OPK Energy</span></p>
    </div>
  </article>

  <article class="panel panel--contact">
    <div class="brand"><span class="brand__dot"></span><span class="brand__name">HARBOR LYNX</span><span class="brand__sub">ASSOCIATES</span></div>
    <h2 class="contact__title">CONTACT US</h2>
    <div class="contact__rule"></div>
    <ul class="contact__list">
      <li class="contact__item contact__item--phone">
        <span class="icon"><svg viewBox="0 0 24 24" fill="none" stroke="#fff" stroke-width="2"><path d="M5 3h4l2 5-2.5 1.5a11 11 0 0 0 6 6L16 13l5 2v4a2 2 0 0 1-2 2A16 16 0 0 1 3 5a2 2 0 0 1 2-2z"/></svg></span>
        0123 - 456 - 789
      </li>
      <li class="contact__item">
        <span class="icon"><svg viewBox="0 0 24 24" fill="none" stroke="#fff" stroke-width="2"><rect x="3" y="5" width="18" height="14" rx="1"/><path d="M3 6l9 7 9-7"/></svg></span>
        info@harborlynxassociates.com
      </li>
      <li class="contact__item">
        <span class="icon"><svg viewBox="0 0 24 24" fill="none" stroke="#fff" stroke-width="2"><circle cx="12" cy="12" r="9"/><path d="M3 12h18M12 3c3 3 3 15 0 18M12 3c-3 3-3 15 0 18"/></svg></span>
        harborlynxassociates.com
      </li>
      <li class="contact__item">
        <span class="icon"><svg viewBox="0 0 24 24" fill="none" stroke="#fff" stroke-width="2"><path d="M12 22s-7-7-7-12a7 7 0 0 1 14 0c0 5-7 12-7 12z"/><circle cx="12" cy="10" r="2.5"/></svg></span>
        <span>address will be here<br>address will be here</span>
      </li>
    </ul>
  </article>

  <article class="panel panel--cover">
    <svg class="photo" style="left:0;top:0" width="207" height="292" viewBox="0 0 207 292">
      <defs>
        <linearGradient id="partnersGrad" x1="0" y1="0" x2="0" y2="1">
          <stop offset="0" stop-color="#c9d8ea"/><stop offset=".35" stop-color="#9fb8d2"/><stop offset=".7" stop-color="#b89a86"/><stop offset="1" stop-color="#5b5e66"/>
        </linearGradient>
      </defs>
      <path d="M0 95Q110 125 207 82V292H0Z" fill="url(#partnersGrad)" role="img" aria-label="Photo of the two partners standing in front of power lines"/>
      <path d="M0 88Q110 120 207 75V82Q110 125 0 95Z" fill="var(--sky)"/>
      <path d="M0 95Q110 125 207 82V87Q110 131 0 101Z" fill="var(--ink)"/>
    </svg>
    <div class="cover__logo brand"><span class="brand__dot"></span><span class="brand__name">HARBOR LYNX</span><span class="brand__sub">ASSOCIATES</span></div>
    <div class="cover__url">HARBORLYNXASSOCIATES.COM</div>
    <div class="cover__stripes"></div>
    <h1 class="cover__headline">RETAIL ENERGY<br><span class="accent">RECRUITING<br>AND</span> M&amp;A<br><span class="accent">CONSULTING</span></h1>
  </article>
</section>

<!-- Inside spread -->
<section class="spread spread--inside" aria-label="Brochure inside">
  <article class="panel panel--about">
    <div class="about__rule"></div>
    <p class="about__kicker">ABOUT</p>
    <h2 class="about__title">Harbor Lynx<br>Associates</h2>
    <div class="about__text">
      <p>Harbor Lynx Associates is the 4th company in the retail energy space started by Marcus &amp; Dana Whitlow. Marcus &amp; Dana have been in the retail energy space for more than 25 years and are two of the most connected people in the industry.</p>
      <p>Harbor Lynx Associates helps companies in two ways. First, HLA is an experienced M&amp;A consulting firm. Whether you’re looking to buy or sell, we can connect you with buyers and sellers that match your target profile. We work with REPs, brokers and retail energy vendors of all types. We’re not investment bankers, but we’re better connected and charge much less. In the last 12 months, HLA has made the introductions for 3 significant transactions. If now is the right time for a strategic move, we can help.</p>
    </div>
  </article>

  <article class="panel panel--mission">
    <div class="brand"><span class="brand__dot"></span><span class="brand__name">HARBOR LYNX</span><span class="brand__sub">ASSOCIATES</span></div>
    <p class="mission__text">Harbor Lynx Associates is also retail energy’s most used recruiter. HLA is the only recruiting company focused exclusively on the retail energy industry. Since our inception in 2022, HLA has filled over 35 roles – including sales, channel management, pricing, billing, supply, regulatory etc. Harbor Lynx Associates works quickly and we can find great talent from analyst level positions right up to the most critical C-level jobs. We help REPs, brokers and retail energy industry vendors find the great people they need to keep growing. Harbor Lynx Associates only works with experienced retail energy professionals.</p>
  </article>

  <article class="panel panel--handshake">
    <svg class="photo" style="left:0;top:0" width="207" height="480" viewBox="0 0 207 480">
      <defs>
        <linearGradient id="handGrad" x1="0" y1="0" x2="1" y2="1">
          <stop offset="0" stop-color="#5a6676"/><stop offset=".45" stop-color="#8fa3b8"/><stop offset=".7" stop-color="#b8a08c"/><stop offset="1" stop-color="#3d4a5a"/>
        </linearGradient>
      </defs>
      <rect width="207" height="480" fill="url(#handGrad)" role="img" aria-label="Photo of two businesspeople shaking hands"/>
    </svg>
  </article>

  <svg class="inside-art" viewBox="0 0 620 480">
    <defs>
      <linearGradient id="linesGrad" x1="0" y1="0" x2="0" y2="1">
        <stop offset="0" stop-color="#9db5cf"/><stop offset=".45" stop-color="#4f6f95"/><stop offset="1" stop-color="#1f3a5c"/>
      </linearGradient>
    </defs>
    <path d="M0 485Q310 155 620 475V480H0Z" fill="url(#linesGrad)" role="img" aria-label="Photo of power line towers against mountains at dusk"/>
    <path d="M0 470Q310 140 620 460V468Q310 148 0 478Z" fill="var(--sky)"/>
    <path d="M0 478Q310 148 620 468V475Q310 155 0 485Z" fill="var(--ink)"/>
  </svg>

  <div class="office" role="img" aria-label="Photo of a modern office with city view"></div>
</section>

</body>
</html>
```